Stationery Required - Own Logo provided

Hi,

We are a retail company called 'Copperfinch Trading Limited' based in the UK and would like some corporate stationery designed.

We have provided our Logo which we would like to use (Its attached to this brief)...

The designs must be orginal, professional, stylish and interesting!

Target Market(s)

We will use this stationery to communicate with our wholesale suppliers and employees, so it must have a 'professional' feel about it.

Industry/Entity Type

It Company

Requirements
Must have
• Must be professional, corporate, stylish and not to 'fussy'. we require ... Business card design, a4 letter, compliment slip. All designs must be supplied in a format where the text (address/telephone numbers etc..) can be edited, as we have alot of staff and operate out of several different premises.
Nice to have
• I would like a windows backround picture file supplied as well so we can integrate that onto our computer systems.

```html
<!DOCTYPE html>
<html lang="en">
<head>
<meta charset="utf-8">
<title>Copperfinch Trading Limited – Letterhead</title>
<link rel="stylesheet" href="https://fonts.googleapis.com/css2?family=Arimo:wght@400;700&display=swap">
<style>
  :root {
    --paper: #ffffff;
    --brand-green: #8cc63e;
    --deep-green: #2f4a1e;
    --mid-green: #5f8f2a;
    --text-grey: #4a4a4a;
  }
  * { margin: 0; padding: 0; box-sizing: border-box; }
  html, body {
    width: 854px;
    height: 1200px;
    overflow: hidden;
    background: var(--paper);
  }
  .letterhead {
    position: relative;
    width: 854px;
    height: 1200px;
    background: var(--paper);
    font-family: "Arimo", Arial, sans-serif;
    color: var(--text-grey);
  }
  .brand {
    position: absolute;
    left: 46px;
    top: 84px;
    display: flex;
    align-items: center;
    gap: 18px;
  }
  .brand__mark {
    width: 88px;
    height: 88px;
    background: var(--deep-green);
  }
  .brand__name {
    font-size: 46px;
    font-weight: 400;
    color: var(--brand-green);
    line-height: 1;
    letter-spacing: -0.5px;
  }
  .decor {
    position: absolute;
  }
  .decor--top-right {
    right: 0;
    top: 0;
    width: 215px;
    height: 225px;
    background: radial-gradient(circle at 80% 25%, var(--deep-green) 0%, var(--mid-green) 35%, var(--brand-green) 58%, rgba(140,198,62,0) 75%);
  }
  .decor--bottom-left {
    left: 0;
    bottom: 0;
    width: 210px;
    height: 240px;
    background: radial-gradient(circle at 20% 78%, var(--deep-green) 0%, var(--mid-green) 35%, var(--brand-green) 58%, rgba(140,198,62,0) 75%);
  }
  .footer-rule {
    position: absolute;
    left: 265px;
    top: 1050px;
    width: 553px;
    height: 4px;
    background: var(--brand-green);
  }
  .contact {
    position: absolute;
    left: 265px;
    top: 1068px;
    font-size: 16px;
    line-height: 23px;
    list-style: none;
  }
  .contact__label,
  .contact__company {
    color: var(--brand-green);
    font-weight: 700;
  }
</style>
</head>
<body>
  <main class="letterhead">
    <header class="brand">
      <div class="brand__mark"></div>
      <div class="brand__name">Copperfinch Trading</div>
    </header>

    <div class="decor decor--top-right" role="img" aria-label="Decorative cluster of green dots"></div>
    <div class="decor decor--bottom-left" role="img" aria-label="Decorative cluster of green dots"></div>

    <div class="footer-rule"></div>
    <ul class="contact">
      <li class="contact__company">Copperfinch Trading Limited</li>
      <li><span class="contact__label">Phone</span> 555-218 907</li>
      <li><span class="contact__label">Adress</span> 17 Millbrook Lane, Ashcombe, County Down BT31 4QP</li>
      <li><span class="contact__label">Mail</span> hello@copperfinchtrading.com</li>
    </ul>
  </main>
</body>
</html>
```